Can Design for Fun, Growing Health Food Brand

We are launching a brand new product, electrolyte seltzer drinks. We want the design to be clean/simple and slightly modern while staying true to our brand identity. Must say "Mineral Hydration" as the product descriptor, sub headline is "Carbonated electrolyte beverage with sea moss and real fruit juice". First flavors will be Watermelon Mint and Mango.

Target Market(s)

Women ages 30-50 who are interested in health wellness/trends

Industry/Entity Type

Health & Wellness

Font styles to use
Sans Serif

Requirements
Must have
• Tall, skinny can, current Brightfen Kelp Logo, use aluminum on can as element in design.
Nice to have
• Be fun, clean and modern. Would like to see the label less busy than our gels.
Should not have
• Avoid putting flavor on bottom 1/5 of can. No gradient color changes. Do not want really detailed or realistic fruit image, prefer drawings or similar.

```html
<!DOCTYPE html>
<html lang="en">
<head>
<meta charset="utf-8">
<title>Brightfen Kelp — Mineral Hydration Can Label</title>
<link rel="stylesheet" href="https://fonts.googleapis.com/css2?family=Oswald:wght@300;400;500;600;700&family=Jost:wght@300;400&display=swap">
<style>
  :root {
    --page: #ffffff;
    --leaf-green: #2f6b3b;
    --deep-green: #1f5a2c;
    --soft-green: #5f9a6c;
    --cream: #f8f4e4;
    --melon: #dc5c5a;
    --melon-light: #fbe2dc;
    --badge-ring: #c85a56;
    --badge-fill: #f3c9c2;
    --wrap-a: #f4dcd4;
    --wrap-b: #e3efdc;
    --wrap-c: #f7e3c6;
  }
  * { box-sizing: border-box; margin: 0; padding: 0; }
  html, body { width: 1200px; height: 1200px; overflow: hidden; background: var(--page); }
  .canvas { position: relative; width: 1200px; height: 1200px; }

  .can-wrap {
    position: absolute; left: 240px; top: 30px; width: 720px; height: 1140px;
    border-radius: 6px;
    background: linear-gradient(160deg, var(--wrap-a) 0%, var(--wrap-c) 45%, var(--wrap-b) 100%);
  }

  .label {
    position: absolute; left: 365px; top: 75px; width: 470px; height: 1050px;
    border-radius: 8px; overflow: hidden; background: var(--cream);
  }
  .label-shapes { position: absolute; inset: 0; }

  .brand {
    position: absolute; top: 40px; left: 0; right: 0; text-align: center;
  }
  .brand-dot {
    display: block; width: 58px; height: 58px; margin: 0 auto 16px;
    border: 3px solid var(--cream); border-radius: 50%;
  }
  .brand-name {
    font-family: "Oswald", sans-serif; font-weight: 400; font-size: 42px;
    letter-spacing: -0.5px; color: var(--cream); line-height: 1;
  }

  .descriptor {
    position: absolute; top: 258px; left: 0; right: 0; text-align: center;
    font-family: "Oswald", sans-serif; font-weight: 700; color: var(--leaf-green);
    line-height: 0.92;
  }
  .descriptor .line-1 { display: block; font-size: 122px; letter-spacing: -1px; }
  .descriptor .line-2 { display: block; font-size: 104px; letter-spacing: -1px; }

  .subhead {
    position: absolute; top: 482px; left: 0; right: 0; text-align: center;
    font-family: "Jost", sans-serif; font-weight: 300; font-size: 27px;
    line-height: 1.4; color: var(--soft-green);
  }
  .subhead strong { font-weight: 400; color: var(--deep-green); }

  .flavor-pill {
    position: absolute; top: 595px; left: 30px; width: 410px; height: 88px;
    border-radius: 22px; background: var(--melon);
    display: flex; align-items: center; justify-content: center;
    font-family: "Oswald", sans-serif; font-weight: 600; font-size: 31px;
    color: var(--melon-light); letter-spacing: -0.2px;
  }

  .claims {
    position: absolute; top: 750px; left: 20px; right: 20px;
    display: flex; justify-content: space-between;
  }
  .claim { width: 140px; text-align: center; }
  .claim-icon {
    width: 62px; height: 62px; margin: 0 auto 12px; border-radius: 50%;
    background: var(--badge-fill); border: 3px solid var(--badge-ring);
    display: flex; align-items: center; justify-content: center;
  }
  .claim-text {
    font-family: "Oswald", sans-serif; font-weight: 400; font-size: 24px;
    line-height: 1.02; color: var(--deep-green); letter-spacing: -0.3px;
  }
  .claim-text.light { font-weight: 300; color: var(--soft-green); }

  .volume {
    position: absolute; bottom: 38px; left: 0; right: 0; text-align: center;
    font-family: "Oswald", sans-serif; font-weight: 300; font-size: 30px;
    letter-spacing: 1.5px; color: var(--cream);
  }
</style>
</head>
<body>
<main class="canvas">
  <div class="can-wrap" role="img" aria-label="Repeating pattern of illustrated watermelon slices, mangoes and mint leaves on white"></div>

  <section class="label">
    <svg class="label-shapes" viewBox="0 0 470 1050" width="470" height="1050" aria-hidden="true">
      <path d="M0 0 H470 V205 C430 225 395 190 350 198 C300 207 270 232 220 222 C170 212 140 190 95 200 C55 208 30 225 0 215 Z" fill="var(--leaf-green)"/>
      <path d="M0 955 C40 935 80 970 130 960 C180 950 210 925 260 935 C310 945 340 970 390 958 C425 950 450 935 470 940 V1050 H0 Z" fill="var(--leaf-green)"/>
    </svg>

    <header class="brand">
      <span class="brand-dot"></span>
      <div class="brand-name">BRIGHTFEN KELP</div>
    </header>

    <h1 class="descriptor">
      <span class="line-1">MINERAL</span>
      <span class="line-2">HYDRATION</span>
    </h1>

    <p class="subhead">Carbonated <strong>Electrolyte</strong> Beverage<br>with Sea <strong>Moss and Real Fruit</strong> Juice</p>

    <div class="flavor-pill">WATERMELON MINT AND MANGO</div>

    <ul class="claims" style="list-style:none">
      <li class="claim">
        <div class="claim-icon">
          <svg width="34" height="34" viewBox="0 0 34 34" aria-hidden="true">
            <path d="M17 30 V16" stroke="var(--deep-green)" stroke-width="2.5" fill="none"/>
            <path d="M17 18 C17 8 24 4 31 4 C31 13 25 18 17 18 Z" fill="none" stroke="var(--deep-green)" stroke-width="2.2"/>
            <path d="M17 22 C17 14 11 10 4 10 C4 18 10 22 17 22 Z" fill="none" stroke="var(--deep-green)" stroke-width="2.2"/>
          </svg>
        </div>
        <div class="claim-text light">PLANT<br>BASED</div>
      </li>
      <li class="claim">
        <div class="claim-icon">
          <svg width="34" height="34" viewBox="0 0 34 34" aria-hidden="true">
            <rect x="3" y="13" width="11" height="11" fill="var(--deep-green)"/>
            <rect x="13" y="5" width="11" height="11" fill="var(--deep-green)"/>
            <rect x="15" y="18" width="11" height="11" fill="var(--deep-green)"/>
            <rect x="27" y="16" width="6" height="3" fill="var(--deep-green)"/>
          </svg>
        </div>
        <div class="claim-text">LOW IN<br>SUGAR</div>
      </li>
      <li class="claim">
        <div class="claim-icon"></div>
        <div class="claim-text">MADE WITH REAL<br>SEA MOSS</div>
      </li>
    </ul>

    <p class="volume">12 FL OZ (355mL)</p>
  </section>
</main>
</body>
</html>
```